presentation slide template in Adobe Indesign

Hi, we need to design a template for presentation slides as well as presentation-like documents in slide format. See our website: marlowvane-partners.example and also graphical profile attached as a file. I've also attached the images used on our web site.
Regards,
Anselm
Updates
Hi, a clarification: this is about a presentation template not a specific presentation based on the web site content. I only supplied the web site for you as a reference. I imagine the result would include a base slide template that can be used for the bulk of the slides in a presentation and then a number of template slides that can be inserted in to a presentation to make it visually more interesting.
Target Market(s)
Management Consulting, Financial Risk Advisory
Requirements
Must have
- End product must be an Adobe InDesign template.

```html
<!DOCTYPE html>
<html lang="en">
<head>
<meta charset="utf-8">
<title>Marlowvane Partners – Services slide</title>
<link rel="stylesheet" href="https://fonts.googleapis.com/css2?family=Gelasio:wght@400&family=Noto+Sans:wght@400;700&display=swap">
<style>
  :root {
    --page: #ffffff;
    --slide: #ffffff;
    --ink: #1e1e1e;
    --accent: #00829e;
    --frame: #c9c9c9;
    --sky-light: #ece6d2;
    --sky-mid: #d9d2b8;
    --sky-cool: #9fb1b6;
    --sky-warm: #d8b8a4;
  }
  * { margin: 0; padding: 0; box-sizing: border-box; }
  html, body {
    width: 1200px;
    height: 800px;
    overflow: hidden;
    background: var(--page);
  }
  .slide {
    position: absolute;
    left: 96px;
    top: 96px;
    width: 1008px;
    height: 610px;
    background: var(--slide);
    border: 1px solid var(--frame);
    overflow: hidden;
  }
  .section-marker {
    position: absolute;
    left: 0;
    top: 35px;
    width: 46px;
    height: 10px;
    background: var(--accent);
  }
  .section-title {
    position: absolute;
    left: 70px;
    top: 30px;
    font-family: "Gelasio", Georgia, serif;
    font-weight: 400;
    font-size: 22px;
    line-height: 28px;
    color: var(--ink);
    letter-spacing: 0.2px;
  }
  .section-body {
    position: absolute;
    left: 70px;
    top: 76px;
    width: 540px;
    font-family: "Noto Sans", Verdana, sans-serif;
    font-size: 15.5px;
    line-height: 19.4px;
    color: var(--ink);
  }
  .brand-name {
    position: absolute;
    right: 34px;
    top: 74px;
    text-align: right;
    font-family: "Gelasio", Georgia, serif;
    font-weight: 400;
    font-size: 29px;
    line-height: 34px;
    color: var(--ink);
    letter-spacing: 1px;
  }
  .web-address {
    position: absolute;
    right: 28px;
    top: 206px;
    font-family: "Noto Sans", Verdana, sans-serif;
    font-weight: 700;
    font-size: 14px;
    letter-spacing: 2.6px;
    color: var(--accent);
  }
  .hero-photo {
    position: absolute;
    left: 0;
    top: 241px;
    width: 1008px;
    height: 369px;
    background:
      radial-gradient(ellipse at 100% 0%, var(--sky-cool) 0%, rgba(159,177,182,0) 45%),
      radial-gradient(ellipse at 100% 100%, var(--sky-warm) 0%, rgba(216,184,164,0) 40%),
      radial-gradient(ellipse at 0% 60%, var(--sky-cool) 0%, rgba(159,177,182,0) 35%),
      linear-gradient(180deg, var(--sky-mid) 0%, var(--sky-light) 55%, var(--sky-mid) 100%);
  }
</style>
</head>
<body>
  <section class="slide">
    <div class="section-marker"></div>
    <h1 class="section-title">SERVICES</h1>
    <p class="section-body">Lorem ipsum dolor sit amet, consectetur adipisicing elit, sed do eiusmod tempor incididunt ut labore et dolore magna aliqua. Ut enim ad minim veniam, quis nostrud exercitation ullamco laboris nisi ut aliquip ex ea commodo consequat. Duis aute irure dolor in reprehenderit in voluptate velit esse cillum dolore eu fugiat nulla pariatur. Excepteur sint occaecat cupidatat non proident, sunt in culpa qui officia deserunt mollit anim id est laborum.</p>
    <div class="brand-name">MARLOWVANE<br>PARTNERS</div>
    <div class="web-address">marlowvane-partners.example</div>
    <div class="hero-photo" role="img" aria-label="Photograph of colourful kites with long ribbon tails flying against a hazy, cloudy sky"></div>
  </section>
</body>
</html>
```